Boutique Jewellery Card [UPDATED] Embossing and Foil

Hi Designers,

What will win you this competition is your input on making my card look very professional and classy

Just some overview information.

I am striving to be the most prestigious jeweller going around specialising in custom designed jewellery, engagement rings and repairs on a bigger budget.

I am spending a lot on the printing including thick cards, rounded corners, multi level embossing and foiling.

Front:

I want my entire logo on the front, which I will have embossed and foiled (source file included)
Optional: I also want a lower embossing of a repeating pattern which I am not sure on. I need YOUR input here

Back:

I need you to use your skills and experience to make my details look very important, professional and classy.

The details I need on the back are:

Marcus Delvaney
Your Jewellery Stylist

www.marcusdelvaney.com
0492 836 514
marcus@marcusdelvaney.com

The font MUST match the font/style used in the logo.
Everything else including layout, whether my logo is on the back etc, engrave/endent, foiling etc is what I need your input for
Updates

Project Deadline Extended Reason: I was a bit slow and out of action at the start, but we're almost there, just need a few more days to finalize Added Sunday, November 16, 2014

Target Market(s)

25 - 80 year olds. Fashion concious. Wealthy

Industry/Entity Type

Printing

Contact Information for Business Card

Marcus Delvaney
Your Jewellery Stylist

0492 836 514
marcus@marcusdelvaney.com
www.marcusdelvaney.com
- facebook and instagram logo's

Requirements
Must have
• Must use the font from my logo on the back, or very similar
• My logo on the front
• My details on the back must be the centre of attention, my logo can still be there but is less important.
• Back must include the facebook and instagram logo's
Nice to have
• repeating pattern or monogram

```html
<!DOCTYPE html>
<html lang="en">
<head>
<meta charset="utf-8">
<title>Marcus Delvaney – Business Card</title>
<link href="https://fonts.googleapis.com/css2?family=Saira+Semi+Condensed:wght@500;600&display=swap" rel="stylesheet">
<style>
  :root {
    --backdrop: #e9e9ea;
    --card-dark: #444246;
    --emboss-light: #58565b;
    --emboss-shade: #2f2e31;
    --card-white: #ffffff;
    --border-grey: #4a484c;
    --ink: #3c3b3f;
  }
  * { margin: 0; padding: 0; box-sizing: border-box; }
  html, body {
    width: 1200px;
    height: 1192px;
    overflow: hidden;
    background: var(--backdrop);
    font-family: "Saira Semi Condensed", "Arial Narrow", sans-serif;
  }
  .canvas {
    width: 1200px;
    height: 1192px;
    display: flex;
    flex-direction: column;
    align-items: center;
    justify-content: center;
    gap: 72px;
  }
  .card {
    width: 840px;
    height: 480px;
    position: relative;
    box-shadow: 0 10px 28px rgba(0,0,0,0.12);
  }

  /* Front face */
  .card-front {
    background: var(--card-dark);
    display: flex;
    flex-direction: column;
    align-items: center;
    justify-content: center;
    gap: 34px;
  }
  .front-mark {
    width: 118px;
    height: 118px;
    border-radius: 50%;
    border: 6px solid var(--emboss-light);
    box-shadow: 0 2px 0 var(--emboss-shade), inset 0 2px 0 var(--emboss-shade);
  }
  .front-name {
    font-weight: 500;
    font-size: 52px;
    letter-spacing: 0.32em;
    text-transform: uppercase;
    color: var(--emboss-light);
    text-shadow: 0 2px 0 var(--emboss-shade);
    padding-left: 0.32em;
  }

  /* Back face */
  .card-back {
    background: var(--card-white);
    border: 26px solid var(--border-grey);
  }
  .details {
    position: absolute;
    left: 230px;
    top: 128px;
    color: var(--ink);
    text-transform: uppercase;
  }
  .details .name {
    font-weight: 600;
    font-size: 38px;
    letter-spacing: 0.16em;
    line-height: 1;
  }
  .details .role {
    font-weight: 600;
    font-size: 17px;
    letter-spacing: 0.2em;
    margin-top: 8px;
    padding-left: 90px;
  }
  .contact {
    list-style: none;
    margin-top: 38px;
    padding-left: 40px;
    font-weight: 500;
    font-size: 18px;
    letter-spacing: 0.16em;
    line-height: 1.55;
  }
  .contact .phone { padding-left: 70px; }
</style>
</head>
<body>
  <main class="canvas">
    <section class="card card-front" aria-label="Card front">
      <div class="front-mark" aria-hidden="true"></div>
      <div class="front-name">Marcus Delvaney</div>
    </section>

    <section class="card card-back" aria-label="Card back">
      <div class="details">
        <h1 class="name">Marcus Delvaney</h1>
        <p class="role">Your Jewellery Stylist</p>
        <ul class="contact">
          <li class="phone">0492 836 514</li>
          <li class="email">marcus@marcusdelvaney.com</li>
          <li class="web">www.marcusdelvaney.com</li>
        </ul>
      </div>
    </section>
  </main>
</body>
</html>
```